LEAP GLIDE SOAR

Need a 4 X 6 post card design. Here are the elements that need to be on the card:
LEAP, GLIDE, SOAR (This is the title please feel free and create)
DATE: August 28, 2022
Showtimes 2:30 PM & 7:30 PM
Location: Harriet Colvane Theatre Walnut Creek, CA
Tickets can be purchased at:
http://colvanestagehall.tixora-example.com/LEAPGLIDESOAR or
by calling the ticket office at (925) 555-STAGE
LEAP, GLIDE, SOAR showcases the dance stylings of urban hip hop, ballet, modern jazz and much much more! Bay Area renown dancer/choreographer Rosa Janelle Pruitt headlines this cast of dancers and will amaze you as she takes you on a journey through dance that you will never forget. Join us for an experience that will prove to excite and delight you!
Now for the artwork I would like to incorporate all three of these photos. The photo entitled "beach" you are only to use the dancer on the left. So clip out the other dancer in the pink dress. The Garden photo and the beach photo the images need to be cut out from the background. The sidewalk photo you can leave the background (just my preference) but for the sake of the overall design I'm ok with removing its background as well.
Ok have at it. I want to end this competition in a few days so let's get these designs in. Thank you!

```html
<!DOCTYPE html>
<html lang="en">
<head>
<meta charset="utf-8">
<title>Leap, Glide, Soar — Postcard</title>
<link href="https://fonts.googleapis.com/css2?family=Lobster&family=Questrial&family=Mulish:ital,wght@0,800;1,800&display=swap" rel="stylesheet">
<style>
  :root {
    --pink: #ec1470;
    --purple-deep: #2c1155;
    --purple-mid: #3d1a76;
    --purple-panel: #6a3b96;
    --white: #ffffff;
    --paper: #ffffff;
  }
  * { margin: 0; padding: 0; box-sizing: border-box; }
  html, body { width: 1200px; height: 847px; overflow: hidden; background: var(--paper); }
  .canvas { position: relative; width: 1200px; height: 847px; }
  .card {
    position: absolute; left: 32px; top: 38px; width: 1137px; height: 774px;
    background: var(--pink); overflow: hidden;
  }
  .card-art { position: absolute; inset: 0; }
  .photo { position: absolute; }
  .photo-headliner {
    left: 48px; top: 208px; width: 146px; height: 440px;
    border-radius: 70px 70px 20px 40px;
    background: linear-gradient(180deg, #3b2a3a 0%, #e06aa8 22%, #e07bb3 80%, #c9a08a 100%);
  }
  .photo-dancer {
    left: 543px; top: 110px; width: 190px; height: 544px;
    border-radius: 90px 90px 30px 30px;
    background: linear-gradient(180deg, #6b4a3a 0%, #1b1b1f 30%, #111114 100%);
  }
  .event-info {
    position: absolute; left: 213px; top: 469px; width: 400px;
    text-align: center; color: var(--white);
    font-family: "Questrial", sans-serif; font-size: 22px; line-height: 27px;
  }
  .event-info strong { font-family: "Mulish", sans-serif; font-weight: 800; font-size: 21px; }
  .venue {
    position: absolute; left: 213px; top: 582px; width: 400px;
    text-align: center; color: var(--white);
    font-family: "Questrial", sans-serif; font-size: 22px; line-height: 28px;
  }
  .venue-pin { position: absolute; left: 201px; top: 548px; }
  .tickets {
    position: absolute; left: 60px; top: 660px; width: 642px;
    text-align: center; color: var(--white);
    font-family: "Questrial", sans-serif; font-size: 18px; line-height: 24px;
  }
  .tickets-lead { font-family: "Mulish", sans-serif; font-weight: 800; font-style: italic; font-size: 17px; }
  .tickets strong { font-family: "Mulish", sans-serif; font-weight: 800; }
  .info-panel {
    position: absolute; left: 734px; top: 228px; width: 359px; height: 546px;
    background: var(--purple-panel); border-radius: 150px 150px 0 0;
    box-shadow: 0 8px 14px rgba(0,0,0,0.35);
  }
  .title-badge {
    position: absolute; left: 772px; top: 56px; width: 296px; height: 296px;
    border-radius: 50%; background: var(--pink);
    display: flex; flex-direction: column; align-items: center; justify-content: center;
  }
  .title-badge h1 {
    font-family: "Lobster", cursive; font-weight: 400; color: var(--white);
    font-size: 52px; line-height: 56px; text-align: center;
  }
  .panel-copy {
    position: absolute; left: 740px; top: 414px; width: 347px;
    text-align: center; color: var(--white);
    font-family: "Questrial", sans-serif; font-size: 19px; line-height: 26.6px;
  }
  .panel-copy h2 { font-family: "Mulish", sans-serif; font-weight: 800; font-size: 22px; line-height: 28px; }
  .panel-copy p + p { margin-top: 26px; }
  .panel-copy em { font-family: "Mulish", sans-serif; font-weight: 800; font-style: italic; }
</style>
</head>
<body>
<div class="canvas">
  <div class="card">
    <svg class="card-art" width="1137" height="774" viewBox="0 0 1137 774">
      <path d="M0,340 C120,440 280,450 380,400 C520,330 590,110 690,0 L980,0 C1060,40 1110,120 1137,210 L1137,652 L0,652 Z" fill="var(--purple-deep)"/>
      <path d="M0,560 C160,520 300,470 420,420 C560,360 640,180 760,60 C820,10 900,-10 980,0 C860,40 780,140 700,300 C620,460 480,520 300,560 C180,585 80,600 0,610 Z" fill="var(--purple-mid)"/>
      <path d="M180,460 C330,470 470,420 560,300 C640,180 700,80 800,30 C720,120 660,260 600,360 C520,470 380,500 180,460 Z" fill="var(--pink)"/>
      <path d="M0,0 L620,0 C540,120 480,330 390,400 C300,470 150,450 60,390 C35,370 15,350 0,330 Z" fill="url(#beachTones)" role="img" aria-label="Photo: dancer in white on a beach, holding a flowing purple scarf overhead"/>
      <defs>
        <linearGradient id="beachTones" x1="0" y1="0" x2="0" y2="1">
          <stop offset="0" stop-color="#b9c2c6"/>
          <stop offset="0.45" stop-color="#8f8a92"/>
          <stop offset="0.7" stop-color="#7a5aa8"/>
          <stop offset="1" stop-color="#a8917d"/>
        </linearGradient>
      </defs>
      <rect x="0" y="652" width="1137" height="122" fill="var(--pink)"/>
    </svg>

    <div class="photo photo-headliner" role="img" aria-label="Cut-out photo: headliner standing in a pink dress"></div>
    <div class="photo photo-dancer" role="img" aria-label="Cut-out photo: dancer in black with arms raised in an arabesque"></div>

    <div class="event-info">
      <div>Date: <strong>August 28, 2022</strong></div>
      <div>Showtimes: <strong>2:30 PM &amp; 7:30 PM</strong></div>
    </div>

    <svg class="venue-pin" width="40" height="54" viewBox="0 0 40 54" aria-hidden="true">
      <path d="M20,2 C9,2 2,10 2,20 C2,32 20,52 20,52 C20,52 38,32 38,20 C38,10 31,2 20,2 Z" fill="var(--pink)"/>
      <circle cx="20" cy="19" r="8" fill="var(--purple-deep)"/>
    </svg>
    <div class="venue">
      <div>Harriet Colvane Theatre</div>
      <div>Walnut Creek, CA</div>
    </div>

    <div class="tickets">
      <div class="tickets-lead">Tickets can be purchased at:</div>
      <div>http://colvanestagehall.tixora-example.com/LEAPGLIDESOAR</div>
      <div>or by calling the ticket office at <strong>(925) 555-STAGE</strong></div>
    </div>

    <div class="info-panel"></div>
    <div class="title-badge">
      <h1>Leap,<br>Glide,<br>Soar</h1>
    </div>
    <div class="panel-copy">
      <p><h2>Leap, Glide, Soar</h2>showcases the dance stylings of urban hip hop, ballet, modern jazz and much much more!</p>
      <p>Bay Area renown dancer/ choreographer <em>Rosa Janelle Pruitt</em> headlines this cast of dancers and will amaze you as she takes you on a journey through dance that you will never forget. Join us for an experience that will prove to excite and delight you!</p>
    </div>
  </div>
</div>
</body>
</html>
```